Supplement Rebranding Bottle Design

READ WORD DOCUMENT ATTACHED.
We want to rebrand our current health supplements (see below). We do want it to be modern, vibrant and appealing. Very upscale and elegant as it targets primarily women.
Bottle size: see pictures for bottle size, along with sample bottles that we like; we’re open to any bottle similar to the ones attached.
Current bottles: So ideally, we’d keep the core color on each bottle with a new branding/bottle design. But we're open to your suggestion.

Target Market(s)

mostly women but shouldn't be overly feminine

Requirements
Must have
• see bottle sizes attached

```html
<!DOCTYPE html>
<html lang="en">
<head>
<meta charset="UTF-8">
<title>Liver Renew Formula – Label</title>
<link href="https://fonts.googleapis.com/css2?family=Outfit:wght@400;500&display=swap" rel="stylesheet">
<style>
  :root {
    --backdrop: #e7e8ea;
    --label: #f6f6f6;
    --band: #d4b8d6;
    --ink: #2a2a2c;
    --ink-soft: #4a4a4e;
  }
  * { margin: 0; padding: 0; box-sizing: border-box; }
  html, body {
    width: 1166px;
    height: 1200px;
    overflow: hidden;
    background: var(--backdrop);
    font-family: "Outfit", sans-serif;
    color: var(--ink);
  }
  .label {
    position: absolute;
    left: 248px;
    top: 60px;
    width: 670px;
    height: 1080px;
    background: var(--label);
    overflow: hidden;
  }
  .color-band {
    position: absolute;
    left: 0;
    top: 305px;
    bottom: 0;
    width: 248px;
    background: var(--band);
  }
  .tagline {
    position: absolute;
    right: 75px;
    top: 240px;
    text-align: right;
    font-size: 20px;
    font-weight: 500;
    line-height: 1.2;
    letter-spacing: -0.2px;
  }
  .product-name {
    position: absolute;
    left: 92px;
    bottom: 164px;
    writing-mode: vertical-rl;
    transform: rotate(180deg);
    font-size: 52px;
    font-weight: 500;
    line-height: 1;
    white-space: nowrap;
    color: var(--ink);
  }
  .supplement-facts {
    position: absolute;
    right: 72px;
    top: 868px;
    text-align: right;
  }
  .supplement-facts__type {
    font-size: 18px;
    font-weight: 400;
    letter-spacing: 4px;
    margin-right: -4px;
  }
  .supplement-facts__count {
    margin-top: 6px;
    font-size: 10px;
    letter-spacing: 1.5px;
    color: var(--ink-soft);
  }
</style>
</head>
<body>
  <main class="label">
    <div class="color-band"></div>
    <p class="tagline">Rejuvenating Cleanse &amp;<br>Detox Formula</p>
    <p class="product-name">Liver Renew Formula</p>
    <div class="supplement-facts">
      <p class="supplement-facts__type">DIETARY SUPPLEMENT</p>
      <p class="supplement-facts__count">120 VEGETABLE CAPSULES</p>
    </div>
  </main>
</body>
</html>
```